Vértice Solar needs the best stationery in the development business

We need a stationary design for a new company based in Porto, Portugal. We are a new property development management company specialized in downtown regeneration projects and adaptive use of old big textile factories.

We just have selected our new logo in a pixelbazaar competition and now we are searching for the best stationary design. We expect to receive proposals for:

Two sided business cards
A4 main letterhead
A4 simple text papper
A4 and A5 envelops
A4 single folder front page

information for the stationary project

company signature: FormaCrescimentoDireção (as in the logo files attached)

Business card information: 
Tomás Vieira Lobato FRICS
Managing Director

email: tomas@verticesolar-exemplo.pt
website: www.verticesolar-exemplo.pt

adress: 
R. das Camélias, 83 - 2º
4050-217 Porto

office number
+(351) 22 418 76 53
fax number
+(351) 22 418 76 59
mobile
+(351) 934 207 615

Target Market(s)

professional finantial fund managers and big property owners

Industry/Entity Type

Business

Requirements
Must have
• the company logo

Nice to have
• clear simple contemporary design is appreciated

```html
<!DOCTYPE html>
<html lang="pt">
<head>
<meta charset="utf-8">
<title>Vértice Solar — Stationery</title>
<link rel="stylesheet" href="https://fonts.googleapis.com/css2?family=Open+Sans:wght@400;600;700&display=swap">
<style>
  :root {
    --brand-blue: #4169a8;
    --ink: #3a3a3a;
    --ink-soft: #6b6b6b;
    --paper: #ffffff;
    --backdrop: #eeeeee;
  }
  * { box-sizing: border-box; margin: 0; padding: 0; }
  html, body { width: 1200px; height: 795px; overflow: hidden; }
  body {
    background: var(--backdrop);
    font-family: "Open Sans", Arial, sans-serif;
    color: var(--ink);
    position: relative;
  }

  /* ---------- Letterhead ---------- */
  .letterhead {
    position: absolute; left: 70px; top: 40px;
    width: 505px; height: 714px;
    background: var(--paper);
    box-shadow: 0 2px 10px rgba(0,0,0,.12);
  }
  .brand { display: flex; align-items: center; gap: 8px; }
  .brand-dot {
    width: 18px; height: 18px; border-radius: 50%;
    background: var(--brand-blue); flex: none;
  }
  .brand-name {
    font-weight: 700; color: var(--brand-blue);
    font-size: 22px; letter-spacing: -.2px; line-height: 1;
    white-space: nowrap;
  }
  .brand-tagline {
    font-size: 7.5px; color: var(--brand-blue);
    margin-top: 3px; margin-left: 26px;
  }
  .letterhead .brand-block { position: absolute; left: 48px; top: 148px; }

  .contact-list { list-style: none; }
  .contact-list li {
    display: flex; align-items: center; gap: 5px;
    font-size: 6.5px; line-height: 10px; color: var(--ink-soft);
    white-space: nowrap;
  }
  .contact-list li.link { color: var(--brand-blue); }
  .contact-icon {
    width: 6px; height: 6px; border-radius: 50%;
    background: var(--brand-blue); flex: none;
  }
  .contact-icon.blank { visibility: hidden; }
  .letterhead .contact-list { position: absolute; right: 40px; top: 44px; }

  .letter-body {
    position: absolute; left: 120px; top: 222px; width: 345px;
    font-size: 8px; line-height: 12px; color: var(--ink-soft);
  }
  .letter-greeting { font-weight: 700; color: var(--ink); margin-bottom: 10px; }
  .letter-body p { margin-bottom: 9px; }
  .letter-body p:last-child { margin-bottom: 0; }

  .signature { position: absolute; left: 120px; top: 548px; }
  .signature-mark {
    width: 120px; height: 32px;
    background: linear-gradient(90deg, #ececec, #f6f6f6);
    border-radius: 3px;
  }
  .signature-role {
    font-size: 8.5px; font-weight: 600; color: var(--ink); margin-top: 4px;
  }

  .band { position: absolute; left: 0; width: 100%; background: var(--brand-blue); }
  .band-upper { top: 612px; height: 9px; }
  .band-lower { top: 676px; height: 7px; }

  /* ---------- Business cards ---------- */
  .card {
    position: absolute; width: 280px; height: 172px;
    box-shadow: 0 2px 8px rgba(0,0,0,.14);
    overflow: hidden;
  }
  .card-front {
    left: 620px; top: 560px; background: var(--brand-blue); color: var(--paper);
  }
  .card-front .emblem {
    position: absolute; left: 26px; top: 20px;
    width: 132px; height: 132px; border-radius: 50%;
    background: var(--paper);
  }
  .card-front .card-brand { position: absolute; right: 18px; top: 76px; text-align: right; }
  .card-front .card-brand-name { font-weight: 700; font-size: 15px; white-space: nowrap; }
  .card-front .card-url { font-size: 7px; margin-top: 3px; white-space: nowrap; }

  .card-back { left: 905px; top: 430px; background: var(--paper); }
  .card-back .brand-block { position: absolute; left: 16px; top: 22px; }
  .card-back .brand-dot { width: 12px; height: 12px; }
  .card-back .brand-name { font-size: 15px; }
  .card-person { position: absolute; left: 16px; top: 66px; }
  .person-name { font-size: 10px; color: var(--ink); white-space: nowrap; }
  .person-role { font-size: 8px; color: var(--ink-soft); margin-top: 2px; }
  .card-rule-h {
    position: absolute; left: 16px; right: 16px; top: 110px;
    height: 1px; background: var(--brand-blue);
  }
  .card-rule-v {
    position: absolute; left: 160px; top: 16px; bottom: 70px;
    width: 1px; background: var(--brand-blue);
  }
  .card-back .phones { position: absolute; left: 16px; top: 120px; }
  .card-back .address { position: absolute; left: 170px; top: 22px; }
  .card-back .contact-list li { font-size: 6px; line-height: 9.5px; }
  .card-back .contact-icon { width: 5px; height: 5px; }
</style>
</head>
<body>

<article class="letterhead">
  <ul class="contact-list">
    <li><span class="contact-icon"></span>+(351) 22 418 76 53</li>
    <li><span class="contact-icon"></span>+(351) 22 418 76 59</li>
    <li><span class="contact-icon"></span>+(351) 934 207 615</li>
    <li><span class="contact-icon"></span>R. das Camélias, 83 - 2º</li>
    <li><span class="contact-icon blank"></span>4050-217 Porto</li>
    <li><span class="contact-icon"></span>tomas@verticesolar-exemplo.pt</li>
    <li class="link"><span class="contact-icon"></span>www.verticesolar-exemplo.pt</li>
  </ul>

  <header class="brand-block">
    <div class="brand"><span class="brand-dot"></span><span class="brand-name">Vértice Solar</span></div>
    <div class="brand-tagline">FormaCrescimentoDireção</div>
  </header>

  <section class="letter-body">
    <p class="letter-greeting">Lorem Ipsum,</p>
    <p>Cras mattis consectetur purus sit amet fermentum. Etiam porta sem malesuada magna mollis euismod. Integer posuere erat a ante venenatis dapibus posuere velit aliquet. Cras justo odio, dapibus ac facilisis in, egestas eget quam. Aenean eu leo quam. Pellentesque ornare sem lacinia quam venenatis vestibulum.</p>
    <p>Vivamus sagittis lacus vel augue laoreet rutrum faucibus dolor auctor. Donec sed odio dui. Etiam porta sem malesuada magna mollis euismod. Morbi leo risus, porta ac consectetur ac, vestibulum at eros. Nullam id dolor id nibh ultricies vehicula ut id elit.</p>
    <p>Donec id elit non mi porta gravida at eget metus. Fusce dapibus, tellus ac cursus commodo, tortor mauris condimentum nibh, ut fermentum massa justo sit amet risus. Cras justo odio, dapibus ac facilisis in, egestas eget quam. Cum sociis natoque penatibus et magnis dis parturient montes, nascetur ridiculus mus.</p>
    <p>Cum sociis natoque penatibus et magnis dis parturient montes, nascetur ridiculus mus. Curabitur blandit tempus porttitor. Aenean lacinia bibendum nulla sed consectetur. Lorem ipsum dolor sit amet, consectetur adipiscing elit.</p>
    <p>Cras justo odio, dapibus ac facilisis in, egestas eget quam. Morbi leo risus, porta ac consectetur ac, vestibulum at eros. Duis mollis, est non commodo luctus, nisi erat porttitor ligula, eget lacinia odio sem nec elit. Integer posuere erat a ante venenatis dapibus posuere velit aliquet. Vivamus sagittis lacus vel augue laoreet rutrum faucibus dolor auctor.</p>
  </section>

  <div class="signature">
    <div class="signature-mark" role="img" aria-label="Handwritten signature of the sender"></div>
    <div class="signature-role">Company Director</div>
  </div>

  <div class="band band-upper"></div>
  <div class="band band-lower"></div>
</article>

<section class="card card-front">
  <div class="emblem"></div>
  <div class="card-brand">
    <div class="card-brand-name">Vértice Solar</div>
    <div class="card-url">www.verticesolar-exemplo.pt</div>
  </div>
</section>

<section class="card card-back">
  <div class="card-rule-v"></div>
  <header class="brand-block">
    <div class="brand"><span class="brand-dot"></span><span class="brand-name">Vértice Solar</span></div>
  </header>
  <div class="card-person">
    <div class="person-name">Tomás Vieira Lobato FRICS</div>
    <div class="person-role">Managing Director</div>
  </div>
  <ul class="contact-list address">
    <li><span class="contact-icon"></span>R. das Camélias, 83 - 2º</li>
    <li><span class="contact-icon blank"></span>4050-217 Porto</li>
    <li><span class="contact-icon"></span>tomas@verticesolar-exemplo.pt</li>
  </ul>
  <div class="card-rule-h"></div>
  <ul class="contact-list phones">
    <li><span class="contact-icon"></span>+(351) 22 418 76 53</li>
    <li><span class="contact-icon"></span>+(351) 22 418 76 59</li>
    <li><span class="contact-icon"></span>+(351) 934 207 615</li>
  </ul>
</section>

</body>
</html>
```